gracefulgemstore.com.au needs a new web design!

We are after a refurbished web design. gracefulgemstore.com.au is an online jewellery store - it represents a brand that is elegant, graceful and superior in quality.

We have colours that we like but are open to new colour schemes. Our favourite colours are teal and cherry (see attached colour story). We also like simple designs with lots of white space.

A website which we love the layout and design is www.velmora.com.au please try and design in a similar fashion.

We require three important pages:

- Home page
- Tiled product category Page (eg. earrings, see current website)
- Single Product Page.

Please be aware we are limited to the current Content Management System for our website so using similiar (but not limited too) layout would be helpful for the lonely developer (me).

Our designer should provide (at least) photoshop files for our disposal with category headings etc being able to be edited as we add or change new product categories.

We have plans to get large photos of models for the home page in the future, but should also be available for large photos of jewellery. Basically we believe photos are essential to sell our product, so please don't be afraid to incorporate some dummy photos into your design. Especially the home page!

We also offer free shipping Australia Wide, please incorporate this into the home page, product and category pages, it needs to show the visitor that it is specifically Free Australian wide shipping.

Other stuff we need:

A cool shipping info button/box (see current single product page)
Some Social networking buttons/boxes for Chatterly and quipster for possible use on home page.

please email oliver@gracefulgemstore.com.au if you have any questions.

Many thanks and we look forward to reviewing your designs.
Updates

Thankyou all for your designs, I have messaged 4 designs which are the front runners. some have been reuqested to make slight adjustments, others have been asked to submit the other pages as per brief.

Cheers,

Oliver

Target Market(s)

Ladies in Australia between the ages of 25 and 55

Industry/Entity Type

Shipping

Requirements
Must have
• Hovers, actions and transitions and potential drop downs
Should not have
• Norvane motion.

```html
<!DOCTYPE html>
<html lang="en">
<head>
<meta charset="utf-8">
<title>Graceful Gem Store – Home</title>
<link href="https://fonts.googleapis.com/css2?family=Ubuntu:wght@400;500&family=Arimo:wght@400;700&display=swap" rel="stylesheet">
<style>
:root{
  --cherry:#e0223f;
  --cherry-dark:#b3172f;
  --teal-light:#9adbe4;
  --teal-mid:#7ccad6;
  --teal-btn:#8fd3df;
  --ink:#222;
  --muted:#444;
  --page:#f7f7f7;
  --white:#fff;
}
*{box-sizing:border-box;margin:0;padding:0}
html,body{width:1011px;height:1200px;overflow:hidden;background:var(--page);font-family:"Arimo",Arial,sans-serif;color:var(--ink)}
.canvas{position:relative;width:1011px;height:1200px}
.sheet{position:absolute;left:87px;top:30px;width:835px;height:1093px;background:var(--white);border-radius:4px;box-shadow:0 0 6px rgba(0,0,0,.25)}
.abs{position:absolute}
.brand{left:124px;top:52px;font-family:"Ubuntu",sans-serif;font-size:38px;color:var(--cherry);font-weight:400;white-space:nowrap}
.shipping{left:746px;top:44px;display:flex;gap:18px;align-items:center}
.shipping .map{width:40px;height:40px;background:#7ccae6;border-radius:6px}
.shipping p{font-family:"Ubuntu",sans-serif;font-size:13px;color:#3b8bbf;line-height:16px}
.account-links{left:599px;top:118px;font-size:11px;color:#444;white-space:nowrap}
.account-links span{margin:0 8px;color:#666}
.cart{left:820px;top:110px;display:flex;gap:8px;align-items:center;font-size:11px;color:#333}
.stage{left:110px;top:147px;width:792px;height:350px;background:linear-gradient(135deg,var(--cherry) 60%,#b91a35);border-radius:4px 4px 0 0}
.nav{left:124px;top:158px;width:767px;height:39px;background:linear-gradient(#fff,#e4e4e4);border-radius:4px;display:flex;align-items:center;padding-left:14px}
.nav a{font-size:12px;color:#222;text-decoration:none;margin-right:39px;transition:color .2s}
.nav a:hover{color:var(--cherry)}
.nav a.active{background:linear-gradient(#ee3a55,var(--cherry));color:#fff;width:82px;height:33px;line-height:33px;text-align:center;border-radius:4px;margin-right:17px}
.hero-photo{left:127px;top:212px;width:483px;height:264px;border-radius:4px;background:radial-gradient(circle at 45% 60%,#fdfcf6 0 18%,#dcdde0 32%,#c9cacd 100%)}
.hero-copy{left:620px;top:253px;width:272px;color:#fff;font-family:"Ubuntu",sans-serif}
.hero-copy h2{font-weight:400;font-size:17px;line-height:32px;text-align:center;text-transform:uppercase;white-space:nowrap}
.hero-copy p{margin:14px 0 0 22px;font-size:12.5px;line-height:27px}
.dots{left:816px;top:452px;display:flex;gap:3px}
.dots i{width:14px;height:14px;border-radius:50%;background:#fff}
.dots i:first-child{background:#8fe0ee}
.main{left:110px;top:497px;width:563px;height:591px;background:var(--teal-light)}
.side{left:673px;top:497px;width:229px;height:591px;background:var(--teal-mid);border-radius:0 0 4px 0}
.band-shadow{left:110px;top:1088px;width:792px;height:16px;background:radial-gradient(ellipse at top,rgba(0,0,0,.35),transparent 70%)}
.welcome{left:129px;top:514px;font-family:"Ubuntu",sans-serif;font-size:20px;color:#222;font-weight:400;padding-bottom:9px;border-bottom:1px dotted #3a7f8a;white-space:nowrap}
.hl{color:var(--cherry)}
.intro{left:133px;top:561px;width:485px;font-size:11px;line-height:19px;color:#222}
.more{left:571px;top:667px;font-size:10px;color:var(--cherry)}
.new-title{left:135px;top:689px;font-family:"Ubuntu",sans-serif;font-size:16px;font-weight:400;padding-bottom:4px;border-bottom:1px dotted #3a7f8a;width:108px;white-space:nowrap}
.card{width:214px;height:311px;top:728px;background:linear-gradient(#ececec,#fff);border-radius:5px;box-shadow:0 0 3px rgba(0,0,0,.2);overflow:hidden}
.card .photo{height:155px;background:linear-gradient(#cfcfcf,#bcbcbc)}
.card h3{font-weight:400;font-size:14px;color:var(--cherry);margin:8px 0 3px 11px}
.card dl{font-size:11px;line-height:25px;margin-left:13px;display:grid;grid-template-columns:78px auto;white-space:nowrap}
.card .btn{position:absolute;right:20px;bottom:10px;width:79px;height:32px;background:linear-gradient(#aee3ec,var(--teal-btn));border:1px solid #6db6c2;border-radius:4px;font-size:11px;text-align:center;line-height:30px}
.pager{left:453px;top:1052px;display:flex;gap:8px;font-size:10px;color:#fff;font-weight:700}
.pager b{width:20px;height:18px;background:var(--cherry);border-radius:3px;text-align:center;line-height:18px}
.pager em{font-style:normal;color:#fff;width:37px}
.side-title{font-size:13px;font-weight:500;color:var(--cherry-dark);font-family:"Ubuntu",sans-serif;white-space:nowrap}
.field{left:692px;width:187px;height:33px;border-radius:6px;background:linear-gradient(#fff,#dcdcdc);font-size:9px;color:#777;padding:12px 0 0 18px}
.submit{left:795px;top:627px;width:83px;height:31px;border:1px solid #555;border-radius:4px;background:linear-gradient(#fff,#ddd);font-size:10px;font-weight:700;text-align:center;line-height:29px}
.rule{left:673px;width:229px;border-top:1px solid #b5e2e9}
.cats{left:710px;top:706px;list-style:none;font-size:11px;line-height:27px}
.cats li::before{content:"›";color:#fff;margin-right:8px}
.offer{left:689px;top:884px;width:199px;height:185px;background:#a9e0e8;border-radius:4px;padding:6px}
.offer .inner{position:relative;height:173px;background:linear-gradient(#f2f2f2,#dedede);border-radius:3px}
.offer .price{position:absolute;left:38px;top:30px;font-family:"Ubuntu",sans-serif;font-size:18px;color:var(--cherry);white-space:nowrap}
.offer .price small{font-size:11px}
.offer .click{position:absolute;right:10px;bottom:10px;font-family:"Ubuntu",sans-serif;font-size:11px;color:var(--cherry);white-space:nowrap}
.pay{left:94px;top:1144px;display:flex;gap:4px}
.pay i,.social i{display:block}
.pay i{width:30px;height:20px;background:#c8c8c8}
.social{left:101px;top:1177px;display:flex;gap:5px}
.social i{width:18px;height:18px;background:#4f7fb8}
.foot-links{left:604px;top:1143px;font-size:11px;color:#222;white-space:nowrap}
.foot-links span{margin:0 14px}
.copy{left:651px;top:1173px;font-size:10px;color:#222;white-space:nowrap}
</style>
</head>
<body>
<div class="canvas">
  <div class="sheet"></div>

  <header>
    <div class="abs brand">Graceful Gem Store</div>
    <div class="abs shipping">
      <div class="map" role="img" aria-label="Small map of Australia"></div>
      <p>FREE SHIPPING<br>AUSTRALIA WIDE</p>
    </div>
    <div class="abs account-links">Login<span>|</span>Create an account<span>|</span>My Cart</div>
    <div class="abs cart">
      <svg width="26" height="30" viewBox="0 0 26 30" aria-hidden="true"><path d="M2 5h4l3 14h13l2-10H8" fill="none" stroke="#666" stroke-width="2"/><circle cx="11" cy="24" r="2.5" fill="#666"/><circle cx="20" cy="24" r="2.5" fill="#666"/></svg>
      <span>(0) Items</span>
    </div>
  </header>

  <section>
    <div class="abs stage"></div>
    <nav class="abs nav">
      <a class="active" href="#">Home</a><a href="#">About&nbsp; Us</a><a href="#">Customer Service</a><a href="#">My Account</a><a href="#">Contact</a>
    </nav>
    <div class="abs hero-photo" role="img" aria-label="Pearl drop pendant on a grey leather background"></div>
    <div class="abs hero-copy">
      <h2>Lorem ipsum dolor sit amet,<br>adipiscing elit.</h2>
      <p>Lorem ipsum dolor sit amet, consectetuer adipiscing elit. Lorem ipsum dolor sit amet, adipiscing&nbsp; elit</p>
    </div>
    <div class="abs dots"><i></i><i></i><i></i><i></i></div>
  </section>

  <main>
    <div class="abs main"></div>
    <div class="abs side"></div>
    <div class="abs band-shadow"></div>

    <h1 class="abs welcome">Welcome to Graceful <span class="hl">Gem Store</span></h1>
    <p class="abs intro">Lorem ipsum dolor sit amet, consectetuer adipiscing elit. Nam nibh. Nunc varius facilisis eros. Sed erat. Lorem ipsum dolor sit amet, consectetuer adipiscing elit. nibh. Nunc varius facilisis eros. Sed erat. Lorem ipsum dolor sit amet, consectetuer adipiscing elit. Nam nibh. Nunc varius facilisis eros. Sed erat. Lorem ipsum dolor sit amet, consectetuer adipiscing elit. Lorem ipsum dolor sit amet, consectetuer adipiscing elit. Nam nibh. Nunc varius facilisis eros.</p>
    <a class="abs more">View More</a>

    <h2 class="abs new-title">New <span class="hl">Products</span></h2>

    <article class="abs card" style="left:146px">
      <div class="photo" role="img" aria-label="Sterling silver earrings with pearl centres"></div>
      <h3>Earrings</h3>
      <dl><dt>Model Name :</dt><dd>Sterling Silver Earrings</dd><dt>Model No&nbsp; :</dt><dd>E0599</dd><dt>Diamond&nbsp;&nbsp; :</dt><dd>Pearl Drop Earrings</dd></dl>
      <div class="btn">DETAILS</div>
    </article>
    <article class="abs card" style="left:409px">
      <div class="photo" role="img" aria-label="Sterling silver box chain bracelet"></div>
      <h3>Bracelets</h3>
      <dl><dt>Model Name :</dt><dd>Sterling Silver Bracelet</dd><dt>Model No&nbsp; :</dt><dd>BR129</dd><dt>Diamond&nbsp;&nbsp; :</dt><dd>Bracelet with Bolt Ring</dd></dl>
      <div class="btn">DETAILS</div>
    </article>

    <div class="abs pager"><b>1</b><b>2</b><b>3</b><em>....</em><b>10</b></div>

    <aside>
      <h4 class="abs side-title" style="left:692px;top:508px">LOGIN</h4>
      <div class="abs field" style="top:538px">USER NAME</div>
      <div class="abs field" style="top:581px">PASSWORD</div>
      <div class="abs submit">SUBMIT</div>
      <div class="abs rule" style="top:665px"></div>
      <h4 class="abs side-title" style="left:692px;top:681px">CATEGORIES</h4>
      <ul class="abs cats"><li>Earrings</li><li>Bracelets</li><li>Necklaces</li><li>Chains</li><li>Pendants</li></ul>
      <div class="abs rule" style="top:846px"></div>
      <h4 class="abs side-title" style="left:692px;top:856px">SPECIAL OFFERS</h4>
      <div class="abs offer"><div class="inner" role="img" aria-label="Silver pendant necklace on special offer">
        <span class="price">$24.00 <small>AUD</small></span>
        <span class="click">CLICK HERE &nbsp;&gt;&gt;</span>
      </div></div>
    </aside>
  </main>

  <footer>
    <div class="abs pay" aria-label="Accepted payment cards"><i></i><i></i><i></i><i></i></div>
    <div class="abs social" aria-label="Social networks"><i></i><i></i><i></i></div>
    <div class="abs foot-links">Privacy Policy<span>|</span>Terms &amp; Conditions<span>|</span>Contact</div>
    <div class="abs copy">© 2012 Gracefulgemstore, All Rights Reserved</div>
  </footer>
</div>
</body>
</html>
```